Business Card & Stationary for Orthodontic Office
Lena Voss Orthodontics
Business Card & Stationary for Orthodontic Office  - Medical
Creative Brief
Professional
See Additional Comments
4127 Marlow Ct Brookhaven Falls, ST 14398
Info@SmileCraftClinics.com
www.SmileCraftClinics.com
The logo contains our DBA name however below should read smaller; Lena Voss D.M.D. M.S. PC Also the NCT attached should be included as well.
(additional locations) Ashgrove 5193 Hollin Ridge Ave. Ashgrove, ST 14387 (716)555-0193 Millbrook 2615 Fenwick Rd. Millbrook, ST 14391 (716)555-0147 Dunmore 58 Lorimer St. Dunmore, ST 14802 (585)555-0126 Halbridge 4712 W. Tarrow St. Halbridge, ST 14906 (585)555-0126
LVBrace LVBrace
*************EDIT TO BRIEF*************** We are no longer requiring the NCT logo instead under Lena Voss D.M.D. M.S. PC it should say; "Board Certified Orthodontist" Obviously this is without the quotations. Also the back side of the business card MUST include the remaining office locations. If your draft is submitted without this information on the back it WILL BE ELIMINATED!
*****PLEASE READ THE BRIEF BEFORE SUBMITTING DESIGNS AS THE NCT LOGO MUST BE INCLUDED******** We need all new office supplies as one of our doctors has retired. Business cards (front and back) Stationary (letterhead, envelopes #10, large flat envelopes 12"x15") Included in the brief is a copy of our current letterhead and business card (front & back) to be used as a base point. Our remaining doctor is young, professional, and very modern. Please let this be reflected in the designs that you present.

```html
<!DOCTYPE html>
<html lang="en">
<head>
<meta charset="utf-8">
<title>Lena Voss Orthodontics – Stationery Set</title>
<link href="https://fonts.googleapis.com/css2?family=Open+Sans:wght@400;600&display=swap" rel="stylesheet">
<style>
:root{
  --frame:#74c043;
  --board:#c8c8c8;
  --paper:#ffffff;
  --green:#6cbd45;
  --blue:#1f9ad6;
  --ink:#4a4a4a;
  --badge:#3c3c3c;
  --shadow:rgba(0,0,0,.18);
}
*{box-sizing:border-box;margin:0;padding:0}
html,body{width:1200px;height:954px;overflow:hidden}
body{background:var(--frame);font-family:"Open Sans",Arial,sans-serif;color:var(--ink);position:relative}
.board{position:absolute;left:20px;top:20px;width:1160px;height:914px;background:var(--board)}
.piece{position:absolute;background:var(--paper);overflow:hidden;box-shadow:2px 3px 8px var(--shadow)}
.wave{position:absolute;left:0;bottom:0;width:100%;display:block}
.brand{display:flex;align-items:center;gap:6px;position:absolute;white-space:nowrap}
.brand-dot{border-radius:50%;background:var(--green);flex:none}
.brand-name{color:var(--blue);font-weight:600;letter-spacing:.04em}
.info{position:absolute;font-size:5.5px;line-height:1.45;color:var(--ink);white-space:nowrap}
.info.right{text-align:right}
.badge{position:absolute;background:var(--badge);border-radius:2px}
.locations{position:absolute;display:flex;gap:12px}
.loc{font-size:5px;line-height:1.4;white-space:nowrap;padding-left:5px;border-left:1.5px solid var(--green)}

.board-brand{right:22px;top:50px}
.board-brand .brand-dot{width:34px;height:34px}
.board-brand .brand-name{font-size:19px}

.letterhead{left:37px;top:104px;width:460px;height:626px}
.letterhead .brand{left:14px;top:16px}
.letterhead .brand-dot{width:16px;height:16px}
.letterhead .brand-name{font-size:9px}
.letterhead .info.right{right:14px;top:14px}
.letterhead .mark{position:absolute;left:130px;top:250px;width:130px;height:130px;border-radius:50%;background:var(--green);opacity:.12}
.letterhead .badge{left:14px;top:528px;width:36px;height:12px}
.letterhead .locations{left:190px;top:516px}

.sleeve{left:531px;top:187px;width:302px;height:408px}
.sleeve .notch{position:absolute;right:-40px;top:150px;width:80px;height:80px;border-radius:50%;background:var(--board)}
.sleeve .brand{left:40px;top:118px}
.sleeve .brand-dot{width:22px;height:22px}
.sleeve .brand-name{font-size:11px}
.sleeve .badge{left:22px;top:285px;width:50px;height:14px}

.disc{position:absolute;left:823px;top:208px;width:310px;height:310px;filter:drop-shadow(2px 3px 5px var(--shadow))}

.envelope{left:575px;top:640px;width:563px;height:227px;border-top:9px solid var(--green)}
.envelope .brand{left:22px;top:26px}
.envelope .brand-dot{width:20px;height:20px}
.envelope .brand-name{font-size:10px}
.envelope .info.right{right:18px;top:22px}
.envelope .badge{left:22px;top:120px;width:44px;height:14px}
.envelope .locations{left:190px;top:112px}

.card{top:748px;width:240px;height:145px}
.card-front{left:63px}
.card-back{left:324px}
.card-front .brand{left:14px;top:14px}
.card-front .brand-dot{width:14px;height:14px}
.card-front .brand-name{font-size:7.5px}
.card-front .info{left:14px;top:42px}
.card-front .badge{left:14px;top:80px;width:34px;height:10px}
.card-back .mark{position:absolute;left:20px;top:14px;width:34px;height:34px;border-radius:50%;background:var(--green)}
.card-back .locations{left:78px;top:12px;flex-direction:column;gap:3px}
</style>
</head>
<body>
<main class="board">

  <div class="brand board-brand"><span class="brand-dot"></span><span class="brand-name">Lena Voss Orthodontics</span></div>

  <section class="piece letterhead">
    <div class="brand"><span class="brand-dot"></span><span class="brand-name">Lena Voss Orthodontics</span></div>
    <div class="info right">Lena Voss D.M.D. M.S. PC<br>Board Certified Orthodontist<br>4127 Marlow Ct<br>Brookhaven Falls, ST 14398<br>Info@SmileCraftClinics.com<br>www.SmileCraftClinics.com</div>
    <div class="mark" role="img" aria-label="Faint brand circle"></div>
    <div class="badge" role="img" aria-label="Certification badge"></div>
    <div class="locations">
      <div class="loc">Ashgrove<br>5193 Hollin Ridge Ave.<br>Ashgrove, ST 14387<br>(716)555-0193</div>
      <div class="loc">Millbrook<br>2615 Fenwick Rd.<br>Millbrook, ST 14391<br>(716)555-0147</div>
      <div class="loc">Dunmore<br>58 Lorimer St.<br>Dunmore, ST 14802<br>(585)555-0126</div>
      <div class="loc">Halbridge<br>4712 W. Tarrow St.<br>Halbridge, ST 14906</div>
    </div>
    <svg class="wave" viewBox="0 0 400 60" preserveAspectRatio="none" height="80"><path d="M0 20 C120 -2 260 40 400 6 L400 12 C260 46 120 6 0 26Z" fill="var(--blue)"/><path d="M0 34 C130 12 260 52 400 20 L400 60 L0 60Z" fill="var(--green)"/></svg>
  </section>

  <section class="piece sleeve">
    <div class="notch"></div>
    <div class="brand"><span class="brand-dot"></span><span class="brand-name">Lena Voss Orthodontics</span></div>
    <div class="badge" role="img" aria-label="Certification badge"></div>
    <svg class="wave" viewBox="0 0 400 60" preserveAspectRatio="none" height="110"><path d="M0 20 C120 -2 260 40 400 6 L400 12 C260 46 120 6 0 26Z" fill="var(--blue)"/><path d="M0 34 C130 12 260 52 400 20 L400 60 L0 60Z" fill="var(--green)"/></svg>
  </section>

  <svg class="disc" viewBox="0 0 310 310" role="img" aria-label="Disc label">
    <defs><clipPath id="disc-clip"><circle cx="155" cy="155" r="154"/></clipPath></defs>
    <g clip-path="url(#disc-clip)">
      <rect width="310" height="310" fill="var(--paper)"/>
      <path d="M0 172 C100 140 200 200 310 150 L310 160 C200 212 100 152 0 182Z" fill="var(--blue)"/>
      <path d="M0 192 C100 162 210 222 310 172 L310 310 L0 310Z" fill="var(--green)"/>
    </g>
    <circle cx="155" cy="155" r="18" fill="var(--board)" stroke="#e4e4e4" stroke-width="6"/>
    <circle cx="112" cy="70" r="8" fill="var(--green)"/>
    <text x="124" y="74" font-family="Open Sans, sans-serif" font-weight="600" font-size="10" fill="var(--blue)">Lena Voss Orthodontics</text>
  </svg>

  <section class="piece envelope">
    <div class="brand"><span class="brand-dot"></span><span class="brand-name">Lena Voss Orthodontics</span></div>
    <div class="info right">Lena Voss D.M.D. M.S. PC<br>Board Certified Orthodontist<br>4127 Marlow Ct<br>Brookhaven Falls, ST 14398<br>www.SmileCraftClinics.com</div>
    <div class="badge" role="img" aria-label="Certification badge"></div>
    <div class="locations">
      <div class="loc">Ashgrove<br>5193 Hollin Ridge Ave.<br>Ashgrove, ST 14387<br>(716)555-0193</div>
      <div class="loc">Millbrook<br>2615 Fenwick Rd.<br>Millbrook, ST 14391<br>(716)555-0147</div>
      <div class="loc">Dunmore<br>58 Lorimer St.<br>Dunmore, ST 14802<br>(585)555-0126</div>
      <div class="loc">Halbridge<br>4712 W. Tarrow St.<br>Halbridge, ST 14906</div>
    </div>
    <svg class="wave" viewBox="0 0 400 60" preserveAspectRatio="none" height="60"><path d="M0 20 C120 -2 260 40 400 6 L400 12 C260 46 120 6 0 26Z" fill="var(--blue)"/><path d="M0 34 C130 12 260 52 400 20 L400 60 L0 60Z" fill="var(--green)"/></svg>
  </section>

  <section class="piece card card-front">
    <div class="brand"><span class="brand-dot"></span><span class="brand-name">Lena Voss Orthodontics</span></div>
    <div class="info">Lena Voss D.M.D. M.S. PC<br>Board Certified Orthodontist<br>4127 Marlow Ct, Brookhaven Falls, ST 14398<br>www.SmileCraftClinics.com</div>
    <div class="badge" role="img" aria-label="Certification badge"></div>
    <svg class="wave" viewBox="0 0 400 60" preserveAspectRatio="none" height="34"><path d="M0 20 C120 -2 260 40 400 6 L400 12 C260 46 120 6 0 26Z" fill="var(--blue)"/><path d="M0 34 C130 12 260 52 400 20 L400 60 L0 60Z" fill="var(--green)"/></svg>
  </section>

  <section class="piece card card-back">
    <div class="mark" role="img" aria-label="Brand circle"></div>
    <div class="locations">
      <div class="loc">Ashgrove · 5193 Hollin Ridge Ave. · (716)555-0193</div>
      <div class="loc">Millbrook · 2615 Fenwick Rd. · (716)555-0147</div>
      <div class="loc">Dunmore · 58 Lorimer St. · (585)555-0126</div>
      <div class="loc">Halbridge · 4712 W. Tarrow St.</div>
    </div>
    <svg class="wave" viewBox="0 0 400 60" preserveAspectRatio="none" height="34"><path d="M0 20 C120 -2 260 40 400 6 L400 12 C260 46 120 6 0 26Z" fill="var(--blue)"/><path d="M0 34 C130 12 260 52 400 20 L400 60 L0 60Z" fill="var(--green)"/></svg>
  </section>

</main>
</body>
</html>
```